Postcard Design

We are Professional, quick and efficient. We are State Licensed and Insured. Gas•Water•Sewer Specializing in all of the customers plumbing needs. We accept credit cards. The law in Louisiana is that I have company address, and license number on all advertising. License number is LMP 4129. Address is 20917 north cedar rd. Cut Off, La. 70512

```html
<!DOCTYPE html>
<html lang="en">
<head>
<meta charset="utf-8">
<title>Plumbing Postcard – Front and Back</title>
<link rel="stylesheet" href="https://fonts.googleapis.com/css2?family=Rajdhani:wght@600;700&family=Varela+Round&display=swap">
<style>
:root{
  --navy:#232266;
  --royal:#35328e;
  --red:#a11c22;
  --gold:#d8a12a;
  --ink:#3a3a3a;
  --paper:#ffffff;
  --mist:#e6e6e6;
  --stamp:#e2e2e2;
  --backdrop:#efeae4;
  --photo-a:#d9dde3;
  --photo-b:#8a8f99;
}
*{box-sizing:border-box;margin:0;padding:0}
html,body{width:825px;height:1200px;overflow:hidden}
body{background:var(--backdrop);position:relative;font-family:"Varela Round",sans-serif}
.card{position:absolute;width:654px;height:424px;overflow:hidden;box-shadow:0 3px 10px rgba(0,0,0,.25)}
.card--front{left:86px;top:131px;background:var(--paper)}
.card--back{left:86px;top:644px;background:var(--paper)}
.card-art{position:absolute;inset:0}
.headline{font-family:"Rajdhani",sans-serif;font-weight:700;color:var(--paper);text-transform:uppercase;line-height:1.15;letter-spacing:.3px;white-space:nowrap}
.front-headline{position:absolute;left:340px;width:310px;top:22px;text-align:center;font-size:28.5px}
.front-payment{position:absolute;left:340px;width:310px;top:95px;text-align:center;font-size:23.5px;color:var(--gold);white-space:nowrap}
.front-services{position:absolute;left:17px;top:298px;font-family:"Rajdhani",sans-serif;font-weight:700;font-size:16.5px;line-height:1.25;text-transform:uppercase;white-space:nowrap}
.front-services .licensed{color:var(--red)}
.front-services .speciality{color:var(--ink)}
.front-address{position:absolute;left:17px;top:348px;font-size:16px;color:var(--red);white-space:nowrap}
.front-divider{position:absolute;left:424px;top:302px;width:1px;height:70px;background:var(--red)}
.brand-name{font-family:"Rajdhani",sans-serif;font-weight:700;color:var(--navy);text-transform:uppercase;line-height:.95;white-space:nowrap}
.front-brand{position:absolute;left:516px;top:305px;font-size:17.5px}
.front-brand span{display:block}
.front-brand .brand-big{font-size:29px;margin-top:3px}
.back-headline{position:absolute;left:32px;top:30px;font-size:29.5px}
.back-brand{position:absolute;left:150px;top:156px;font-size:26px}
.back-brand span{display:block}
.back-brand .brand-big{font-size:43px;margin-top:6px}
.back-details{position:absolute;left:32px;top:280px;color:var(--paper);font-size:17.5px;line-height:1.5;white-space:nowrap}
.back-details .license{font-size:20px;margin-bottom:2px}
</style>
</head>
<body>

<section class="card card--front" aria-label="Postcard front">
  <svg class="card-art" width="654" height="424" viewBox="0 0 654 424">
    <defs>
      <linearGradient id="photoTone" x1="0" y1="0" x2="1" y2="1">
        <stop offset="0" stop-color="var(--photo-a)"/>
        <stop offset="1" stop-color="var(--photo-b)"/>
      </linearGradient>
      <linearGradient id="panelTone" x1="0" y1="0" x2="0" y2="1">
        <stop offset="0" stop-color="var(--royal)"/>
        <stop offset="1" stop-color="var(--navy)"/>
      </linearGradient>
      <linearGradient id="floorTone" x1="0" y1="0" x2="0" y2="1">
        <stop offset="0" stop-color="var(--mist)"/>
        <stop offset=".5" stop-color="var(--paper)"/>
        <stop offset="1" stop-color="var(--mist)"/>
      </linearGradient>
    </defs>
    <rect class="hero-photo" x="0" y="0" width="330" height="240" fill="url(#photoTone)" role="img" aria-label="Photo of a plumber repairing pipes under a sink"/>
    <polygon class="accent-diagonal" points="304,0 318,0 338,240 322,240" fill="var(--red)"/>
    <polygon class="message-panel" points="318,0 654,0 654,240 338,240" fill="url(#panelTone)"/>
    <path class="swoosh-red" d="M0,206 Q327,230 654,206 L654,246 L0,246 Z" fill="var(--red)"/>
    <path class="swoosh-blue" d="M0,222 Q327,250 654,222 L654,262 L0,262 Z" fill="var(--royal)"/>
    <path class="floor" d="M0,240 Q327,222 654,240 L654,389 L0,389 Z" fill="url(#floorTone)"/>
    <g class="service-photos">
      <circle cx="159" cy="211" r="56" fill="var(--red)"/>
      <circle cx="159" cy="211" r="53" fill="var(--paper)"/>
      <circle cx="159" cy="211" r="48" fill="url(#photoTone)" role="img" aria-label="Photo of a technician servicing an air unit"/>
      <circle cx="329" cy="211" r="56" fill="var(--red)"/>
      <circle cx="329" cy="211" r="53" fill="var(--paper)"/>
      <circle cx="329" cy="211" r="48" fill="url(#photoTone)" role="img" aria-label="Photo of a plumber tightening a pipe fitting"/>
      <circle cx="491" cy="211" r="56" fill="var(--red)"/>
      <circle cx="491" cy="211" r="53" fill="var(--paper)"/>
      <circle cx="491" cy="211" r="48" fill="url(#photoTone)" role="img" aria-label="Photo of a plumber working on drain pipes"/>
    </g>
    <rect class="footer-rule" x="0" y="389" width="654" height="7" fill="var(--red)"/>
    <rect class="footer-band" x="0" y="396" width="654" height="28" fill="var(--navy)"/>
  </svg>

  <h1 class="headline front-headline">We are professional<br>quick and efficient</h1>
  <p class="front-payment">We accept credit cards</p>
  <p class="front-services">
    <span class="licensed">We are state licensed and insured. Gas•Water•Sewer</span><br>
    <span class="speciality">Specializing in all of the customers plumbing needs</span>
  </p>
  <p class="front-address">Address is 20917 north cedar rd. Cut Off, La. 70512</p>
  <div class="front-divider"></div>
  <p class="brand-name front-brand"><span>Your Plumbing</span><span class="brand-big">Company</span></p>
</section>

<section class="card card--back" aria-label="Postcard back">
  <svg class="card-art" width="654" height="424" viewBox="0 0 654 424">
    <rect class="headline-block" x="0" y="0" width="350" height="132" fill="var(--royal)"/>
    <rect class="brand-block" x="0" y="132" width="350" height="125" fill="var(--paper)"/>
    <rect class="details-block" x="0" y="257" width="350" height="130" fill="var(--navy)"/>
    <rect class="divider-bar" x="350" y="0" width="9" height="387" fill="var(--red)"/>
    <rect class="address-side" x="359" y="0" width="295" height="387" fill="var(--paper)"/>
    <rect class="stamp-box" x="566" y="28" width="63" height="62" fill="var(--stamp)"/>
    <rect class="footer-band" x="0" y="387" width="654" height="37" fill="var(--red)"/>
  </svg>

  <h2 class="headline back-headline">We are professional<br>quick and efficient</h2>
  <p class="brand-name back-brand"><span>Your Plumbing</span><span class="brand-big">Company</span></p>
  <div class="back-details">
    <p class="license">License number is LMP 4129</p>
    <p>Address is 20917 north cedar rd.<br>Cut Off, La. 70512</p>
  </div>
</section>

</body>
</html>
```